Upscale business cards needed for family business

We need professional business cards created for several family members. We are a family business holding company. We would like these relatively simple and straightforward, but also with a unique element to set them apart. Probably stick with neutral and simple colors - white, grey etc. We need space for the traditional elements, including name, title, address, email/phone number. And we will be creating several from this template so it needs to be template that is easy to switch information in and out of.

Industry/Entity Type

Business

Contact Information for Business Card

Please include the attached Dunmore Ventures logo.

Requirements
Must have
• The attached Dunmore Ventures logo.

```html
<!DOCTYPE html>
<html lang="en">
<head>
<meta charset="utf-8">
<title>Dunmore Ventures – Business Cards</title>
<link href="https://fonts.googleapis.com/css2?family=Cinzel:wght@400;600&family=Lato:wght@400&display=swap" rel="stylesheet">
<style>
  :root {
    --bg: #3c3c3c;
    --card-dark: #232222;
    --card-light: #ffffff;
    --gold: #d9a92c;
    --gold-soft: #e4b73f;
    --text-light: #f1f1f1;
    --text-grey: #b9b9b9;
    --text-dark: #2b2b2b;
  }
  * { margin: 0; padding: 0; box-sizing: border-box; }
  html, body { width: 1200px; height: 810px; overflow: hidden; background: var(--bg); }
  .canvas {
    position: relative; width: 1200px; height: 810px;
  }
  .card {
    position: absolute; width: 640px; height: 366px; overflow: hidden;
    box-shadow: 0 10px 24px rgba(0,0,0,.35);
  }
  .card-front {
    left: 180px; top: 30px; background: var(--card-dark);
    display: flex; flex-direction: column; align-items: center; justify-content: center;
  }
  .card-back { left: 380px; top: 414px; background: var(--card-dark); }

  .brand-name {
    font-family: "Cinzel", serif; font-weight: 400; letter-spacing: 2px;
    text-align: center; line-height: 1;
  }
  .card-front .brand-name { color: var(--text-light); font-size: 40px; }
  .front-url {
    margin-top: 44px; font-family: "Lato", sans-serif; font-size: 15px; color: var(--gold);
  }

  .back-brand-panel {
    position: absolute; left: 0; top: 0; width: 258px; height: 100%;
    background: var(--card-light);
    display: flex; align-items: center; justify-content: center;
  }
  .back-brand-panel .brand-name { color: var(--text-dark); font-size: 23px; letter-spacing: 1.5px; }
  .gold-band { position: absolute; left: 258px; top: 0; width: 11px; height: 100%; background: var(--gold); }
  .gold-tab {
    position: absolute; left: 262px; top: 52px; width: 18px; height: 38px;
    background: var(--gold); border-radius: 0 6px 6px 0;
  }

  .contact-block { position: absolute; left: 312px; top: 50px; right: 20px; }
  .person-name {
    font-family: "Cinzel", serif; font-weight: 600; font-size: 22px;
    color: var(--gold); letter-spacing: 1px;
  }
  .person-title {
    font-family: "Lato", sans-serif; font-size: 15px; color: var(--text-light); margin-top: 2px;
  }
  .address {
    font-family: "Lato", sans-serif; font-size: 15px; color: var(--text-light);
    margin-top: 50px; line-height: 1.45;
  }
  .contact-list { list-style: none; margin-top: 34px; }
  .contact-list li {
    display: flex; align-items: center; gap: 10px;
    font-family: "Lato", sans-serif; font-size: 15px; color: var(--text-light); line-height: 1.5;
  }
  .contact-list svg { width: 14px; height: 14px; flex: none; fill: var(--gold); }
</style>
</head>
<body>
<main class="canvas">

  <section class="card card-front">
    <div class="brand-name">Dunmore Ventures</div>
    <div class="front-url">www.dunmoreventuresinc.com</div>
  </section>

  <section class="card card-back">
    <div class="back-brand-panel">
      <div class="brand-name">Dunmore Ventures</div>
    </div>
    <div class="gold-band"></div>
    <div class="gold-tab"></div>

    <div class="contact-block">
      <div class="person-name">Adrian Cole</div>
      <div class="person-title">President @ CEO</div>

      <div class="address">Suite 210, Harbor Lane<br>Lakewood, USA 90712</div>

      <ul class="contact-list">
        <li>
          <svg viewBox="0 0 24 24" aria-hidden="true"><path d="M6.6 10.8a15 15 0 0 0 6.6 6.6l2.2-2.2a1 1 0 0 1 1-.25 11.4 11.4 0 0 0 3.6.57 1 1 0 0 1 1 1V20a1 1 0 0 1-1 1A17 17 0 0 1 3 4a1 1 0 0 1 1-1h3.5a1 1 0 0 1 1 1c0 1.25.2 2.45.57 3.57a1 1 0 0 1-.25 1z"/></svg>
          (000) 000 0000
        </li>
        <li>
          <svg viewBox="0 0 24 24" aria-hidden="true"><path d="M7 1h10a2 2 0 0 1 2 2v18a2 2 0 0 1-2 2H7a2 2 0 0 1-2-2V3a2 2 0 0 1 2-2zm0 3v14h10V4zm5 15.5a1 1 0 1 0 0 2 1 1 0 0 0 0-2z"/></svg>
          (000) 000 0000
        </li>
        <li>
          <svg viewBox="0 0 24 24" aria-hidden="true"><path d="M2 5h20v14H2zm2 2v.5l8 5 8-5V7zm0 2.8V17h16V9.8l-8 5z"/></svg>
          info@dunmoreventuresinc.com
        </li>
        <li>
          <svg viewBox="0 0 24 24" aria-hidden="true"><path d="M12 2a10 10 0 1 0 0 20 10 10 0 0 0 0-20zm6.9 6h-3a15 15 0 0 0-1.3-3.9A8 8 0 0 1 18.9 8zM12 4a13 13 0 0 1 1.9 4h-3.8A13 13 0 0 1 12 4zM4.3 14a8 8 0 0 1 0-4h3.4a16 16 0 0 0 0 4zm.8 2h3a15 15 0 0 0 1.3 3.9A8 8 0 0 1 5.1 16zm3-8h-3a8 8 0 0 1 4.3-3.9A15 15 0 0 0 8.1 8zM12 20a13 13 0 0 1-1.9-4h3.8A13 13 0 0 1 12 20zm2.3-6H9.7a14 14 0 0 1 0-4h4.6a14 14 0 0 1 0 4zm.3 5.9a15 15 0 0 0 1.3-3.9h3a8 8 0 0 1-4.3 3.9zm1.7-5.9a16 16 0 0 0 0-4h3.4a8 8 0 0 1 0 4z"/></svg>
          www.dunmoreventuresinc.com
        </li>
      </ul>
    </div>
  </section>

</main>
</body>
</html>
```